New Flyer Design Project Larkspur Panels and Spaces

Real photos will be added but please start with these for layout. Copy will be supplied so you can just leave a text box to start I am open to suggestions. Thank you

Target Market(s)

Builders, Designers, remodelers, consumers

Colors

Designer to choose colors to be used in the design.

Requirements
Must have
• Before and after photos, email, phone, logo, description

```html
<!DOCTYPE html>
<html lang="en">
<head>
<meta charset="utf-8">
<title>Larkspur Panels and Spaces – Flyer</title>
<link rel="stylesheet" href="https://fonts.googleapis.com/css2?family=Oswald:wght@200;300;400&family=Source+Sans+3:wght@400;600&display=swap">
<style>
  :root{
    --stage:#bcbdbf;
    --paper:#ffffff;
    --paper-soft:#f3f3f3;
    --slate:#4b4b4d;
    --slate-dark:#3f3f41;
    --teal:#67aaa7;
    --teal-text:#6fb1ad;
    --ink:#444446;
    --body:#5a5a5c;
    --white:#ffffff;
  }
  *{box-sizing:border-box;margin:0;padding:0}
  html,body{width:1200px;height:780px;overflow:hidden}
  body{background:var(--stage);position:relative;font-family:"Source Sans 3",Arial,sans-serif;color:var(--body)}
  .page{position:absolute;top:42px;width:521px;height:674px;background:var(--paper);overflow:hidden}
  .page--front{left:54px}
  .page--back{left:626px;background:var(--paper-soft)}

  /* front */
  .brand-mark{position:absolute;left:40px;top:22px;width:140px;text-align:center;color:var(--ink);line-height:1}
  .brand-mark__name{font-size:34px;font-weight:600;display:block}
  .brand-mark__sub{font-size:10px;font-weight:600;letter-spacing:1px;display:block;margin-top:4px}
  .lower-tone{position:absolute;left:0;top:323px;width:521px;height:294px;background:var(--paper-soft)}
  .intro-block{position:absolute;left:0;top:110px;width:263px;height:172px;background:var(--slate);border-top:2px solid #5d7a74}
  .intro-block__title{position:absolute;left:20px;top:10px;width:236px;font-family:"Oswald",Arial,sans-serif;font-weight:300;font-size:25px;line-height:33px;color:var(--teal-text);letter-spacing:-.4px;white-space:nowrap}
  .services{position:absolute;left:23px;top:87px;list-style:none;color:var(--white);font-size:15px;line-height:19px}
  .tagline-bar{position:absolute;left:0;top:282px;width:235px;height:29px;background:var(--teal);color:var(--white);font-size:15px;line-height:29px;padding-left:21px}
  .side-slab{position:absolute;left:517px;top:110px;width:4px;height:191px;background:var(--slate)}
  .hero-photo{position:absolute;left:266px;top:16px;width:248px;height:307px;border:2px solid #d5d5d5;background:linear-gradient(160deg,#e9e1d3 0%,#a88a63 45%,#5b3d25 100%)}
  .swatch{position:absolute}
  .swatch--door-a{left:40px;top:352px;width:40px;height:116px;background:linear-gradient(#4a3524,#6b4f36)}
  .swatch--door-b{left:119px;top:352px;width:44px;height:116px;background:linear-gradient(#707070,#8c8c88)}
  .swatch--door-c{left:201px;top:352px;width:43px;height:116px;background:linear-gradient(#6e4a33,#8a6448)}
  .swatch--iron-a{left:21px;top:481px;width:114px;height:119px;background:linear-gradient(135deg,#ddd3c3,#b9a890)}
  .swatch--iron-b{left:150px;top:481px;width:115px;height:119px;background:radial-gradient(circle,#a88d6c,#6a5440)}
  .description{position:absolute;left:285px;top:350px;width:231px;font-size:10.5px;line-height:13.4px;text-align:justify;color:var(--body)}
  .description p+p{margin-top:12px}

  .contact-bar{position:absolute;left:0;top:617px;width:521px;height:57px;background:var(--teal);border-top:3px solid var(--slate-dark);color:var(--white);font-size:14.5px}
  .contact-bar__item{position:absolute;top:17px;display:flex;align-items:center;gap:8px;white-space:nowrap}
  .contact-bar__item--mail{left:20px}
  .contact-bar__item--web{left:275px}
  .contact-bar svg{width:12px;height:12px}

  /* back */
  .feature-mark{position:absolute;left:60px;top:110px;width:400px;text-align:center;color:var(--ink);line-height:1}
  .feature-mark__name{font-size:96px;font-weight:600;display:block}
  .feature-mark__sub{font-size:28px;font-weight:600;letter-spacing:2px;display:block;margin-top:14px}
  .social{position:absolute;top:359px;width:39px;height:39px;border-radius:5px;background:var(--teal)}
  .social--a{left:214px}
  .social--b{left:270px}
  .handle{position:absolute;left:0;top:418px;width:521px;text-align:center;font-size:14px;color:var(--body)}
  .people{position:absolute;left:0;top:479px;width:521px;text-align:center;font-size:18px;line-height:33px;color:var(--body)}
</style>
</head>
<body>
  <section class="page page--front">
    <div class="lower-tone"></div>
    <div class="brand-mark">
      <span class="brand-mark__name">Larkspur</span>
      <span class="brand-mark__sub">PANELS &amp; SPACES</span>
    </div>
    <div class="side-slab"></div>
    <div class="hero-photo" role="img" aria-label="Photo of a furnished living room with tall antique double doors"></div>
    <div class="intro-block">
      <h1 class="intro-block__title">LARKSPUR PANELS AND<br>INTERIOR RESTORATION</h1>
      <ul class="services">
        <li>VINTAGE DECOR</li>
        <li>IRON ARTS</li>
        <li>ANTIQUE DOORS</li>
        <li>INTERIOR DECOR</li>
      </ul>
    </div>
    <div class="tagline-bar">HOME IMPROVEMENT</div>

    <div class="swatch swatch--door-a" role="img" aria-label="Photo of a dark wood door with iron grille"></div>
    <div class="swatch swatch--door-b" role="img" aria-label="Photo of a weathered grey double door"></div>
    <div class="swatch swatch--door-c" role="img" aria-label="Photo of a carved wood panel door"></div>
    <div class="swatch swatch--iron-a" role="img" aria-label="Photo of scrolled ironwork on a pale wood door"></div>
    <div class="swatch swatch--iron-b" role="img" aria-label="Photo of a round iron scroll window in wood"></div>

    <div class="description">
      <p>Inspired by her travels around the world, interior and showroom designer Maren Holt has put together a unique collection of vintage doors which will create a stunning architectural focal point in any room. Her first collection features individually designed solid wood doors reproduced in Mexico with a faux finish to give a beautifully aged look.</p>
      <p>Exquisite design details such as feature moldings, rare original ironwork and traditional raised field­ed panels complete this timeless vintage look. There are 11 styles of interior doors in a range of colors and finishes. The doors come in standard sizes and custom sized doors can also be made to fit any space. If you are looking to replace those plain doors with an affordable piece of architectur­al art then look no further than Larkspur Panels and Spaces.</p>
    </div>

    <footer class="contact-bar">
      <span class="contact-bar__item contact-bar__item--mail">
        <svg viewBox="0 0 12 12" fill="none" stroke="#fff" stroke-width="1.2"><path d="M1 5l5-3.5L11 5v6H1z"/><path d="M1 5l5 3.5L11 5"/></svg>
        larkspurpanels@mail
      </span>
      <span class="contact-bar__item contact-bar__item--web">
        <svg viewBox="0 0 12 12" fill="none" stroke="#fff" stroke-width="1"><circle cx="6" cy="6" r="5"/><ellipse cx="6" cy="6" rx="2.2" ry="5"/><path d="M1 6h10"/></svg>
        www.larkspurpanels.com
      </span>
    </footer>
  </section>

  <section class="page page--back">
    <div class="feature-mark">
      <span class="feature-mark__name">Larkspur</span>
      <span class="feature-mark__sub">PANELS &amp; SPACES</span>
    </div>
    <span class="social social--a" aria-hidden="true"></span>
    <span class="social social--b" aria-hidden="true"></span>
    <p class="handle">larkspurpanels</p>
    <div class="people">
      <p>Maren Holt 555-214-7830</p>
      <p>Elias Holt 555-308-2619</p>
    </div>
    <footer class="contact-bar">
      <span class="contact-bar__item contact-bar__item--mail">
        <svg viewBox="0 0 12 12" fill="none" stroke="#fff" stroke-width="1.2"><path d="M1 5l5-3.5L11 5v6H1z"/><path d="M1 5l5 3.5L11 5"/></svg>
        larkspurpanels@mail
      </span>
      <span class="contact-bar__item contact-bar__item--web">
        <svg viewBox="0 0 12 12" fill="none" stroke="#fff" stroke-width="1"><circle cx="6" cy="6" r="5"/><ellipse cx="6" cy="6" rx="2.2" ry="5"/><path d="M1 6h10"/></svg>
        www.larkspurpanels.com
      </span>
    </footer>
  </section>
</body>
</html>
```